New modern business card design

To design a brand new business card that's clean & modern in terms of layout.
I have attached our company logo and also basic information regarding what is needed on the card that also needs to be editable.

Target Market(s)

motor trade

Contact Information for Business Card

logo, name, title, tel, mob, email, address, www, all information is in the word.doc file

Requirements
Must have
• white background
Nice to have
• Nice clean font

```html
<!DOCTYPE html>
<html lang="en">
<head>
<meta charset="utf-8">
<title>Torque Fix Ltd – Business Card</title>
<link rel="stylesheet" href="https://fonts.googleapis.com/css2?family=Michroma&family=Open+Sans:wght@400;600&display=swap">
<style>
  :root {
    --backdrop: #2f2f30;
    --card-white: #ececec;
    --brand-blue: #1f74bb;
    --brand-grey: #a7a8ab;
    --ink: #4a4a4a;
    --rule: #8a8a8a;
    --white: #ffffff;
  }
  * { margin: 0; padding: 0; box-sizing: border-box; }
  html, body { width: 1200px; height: 1200px; overflow: hidden; }
  body {
    background: var(--backdrop);
    position: relative;
    font-family: "Open Sans", Arial, sans-serif;
  }
  .card {
    position: absolute;
    top: 310px;
    height: 594px;
    box-shadow: 0 2px 6px rgba(0,0,0,0.45);
    overflow: hidden;
  }
  .card-front {
    left: 234px;
    width: 364px;
    background: var(--card-white);
    text-align: center;
    color: var(--ink);
  }
  .card-back {
    left: 627px;
    width: 369px;
    background: var(--brand-blue);
  }
  .wordmark {
    position: absolute;
    left: 0; right: 0;
    top: 470px;
    top: 160px;
    display: flex;
    justify-content: center;
    align-items: center;
    gap: 10px;
    font-weight: 600;
    font-size: 27px;
    letter-spacing: 1px;
    color: var(--brand-blue);
  }
  .wordmark-square {
    width: 22px; height: 22px;
    background: var(--brand-blue);
  }
  .person-name {
    position: absolute;
    left: 0; right: 0;
    top: 310px;
    font-family: "Michroma", "Open Sans", sans-serif;
    font-size: 19px;
    color: var(--brand-blue);
    letter-spacing: 0.5px;
  }
  .person-title {
    position: absolute;
    left: 0; right: 0;
    top: 335px;
    font-size: 17px;
  }
  .rule {
    position: absolute;
    left: 74px;
    width: 216px;
    height: 1px;
    background: var(--rule);
  }
  .rule-upper { top: 367px; }
  .rule-lower { top: 475px; }
  .info-block {
    position: absolute;
    left: 0; right: 0;
    font-size: 17px;
    line-height: 21px;
  }
  .address { top: 376px; }
  .contacts { top: 489px; }
  .link { color: var(--brand-blue); }
  .label { color: var(--brand-blue); }
  .faint-web { color: var(--white); }
  .back-top {
    position: absolute;
    left: 0; top: 0;
    width: 100%; height: 205px;
    background: var(--brand-grey);
  }
  .back-name {
    position: absolute;
    left: 0; right: 0;
    top: 270px;
    text-align: center;
    font-weight: 600;
    font-size: 36px;
    letter-spacing: 1px;
    color: var(--white);
  }
  .back-web {
    position: absolute;
    left: 0; right: 0;
    top: 538px;
    text-align: center;
    font-weight: 600;
    font-size: 17px;
    color: var(--white);
  }
</style>
</head>
<body>
  <section class="card card-front">
    <div class="wordmark"><span class="wordmark-square"></span><span>TORQUE FIX LTD</span></div>
    <div class="person-name">DANIEL HARTLEY</div>
    <div class="person-title">General Manager</div>
    <div class="rule rule-upper"></div>
    <div class="info-block address">
      Kingsway Road<br>
      Denton, Manchester<br>
      M99 4QT<br>
      <span class="link">www.torque-fix.co.uk</span>
    </div>
    <div class="rule rule-lower"></div>
    <div class="info-block contacts">
      <span class="label">P:</span> 0161 000 4821<br>
      <span class="label">M:</span> 07700 900 412<br>
      <span class="label">E:</span> dhartley@torque-fix.co.uk<br>
      <span class="faint-web">www.torque-fix.co.uk</span>
    </div>
  </section>

  <section class="card card-back">
    <div class="back-top"></div>
    <div class="back-name">TORQUE FIX</div>
    <div class="back-web">www.torque-fix.co.uk</div>
  </section>
</body>
</html>
```